Comic, writer, and entrepreneur based in Los Angeles, CA

UPDATED BRIEF:

Need a PROFESSIONAL yet simultaneously sexy business card that will inspire those to go to my social media accounts and follow me.

Need all of my social media (logos on card, please) As well as my picture, which I will provide.

If there is a way where you could scan the business card from your phone and it would take you to the social media accounts that would be great too!

My goal is to get a comedy writing job at the Nightly Desk or WLR and also go on Pelican Pond once my app is fully functional and created.

But the business card is just something to give people when I am making connections in both the entrepreneurial world as well as the comedy world so it has to help me stand out in that way :).

#: 417-552-8904
Email: kbellin@mx.ovrk.edu
Pictogram: Rosalind_Q.K
Chirpr: @ThePalermoNotes
Craftlo: Rosa’s Clever Tops (website: https://www.craftlo-example.com/shop/RosasTp?ref=pr_shop_more)
VidStream: The Gagmistress (website: https://www.vidstream-example.com/channel/QRpLwVn4kZ-mTHbyqo8erxt7B )
Friendlink: /rosalind.bellin.71924
Website App: WarmFixerFolk.example (app in progress. Need emails to make a prototype.)

Target Market(s)

Talent agents needing TV writers and TV comedy personalities. Investors for my app.

Industry/Entity Type

Tv

Contact Information for Business Card

Can be double or single sided, whichever looks best. Green is my favorite color but I am open to anything. Maybe silver and green?! Just make it classy and sexy.

Colors

Designer to choose colors to be used in the design.

Requirements
Must have
• Chirpr: ThePalermoNotes
• Pictogram: Rosalind_q.k
• Vidstream: The Gagmistress
• Email: kbellin@mx.ovrk.edu
• Phone: 417-552-8904
• writer, comic, entrepreneur--or--comedy writer and entrepeneur
Nice to have
• Make me standout. I'm a star ;-). Please check out my social media for files or ideas. Thanks.

```html
<!DOCTYPE html>
<html lang="en">
<head>
<meta charset="utf-8">
<title>Business Card – Rosalind</title>
<link rel="stylesheet" href="https://fonts.googleapis.com/css2?family=Arimo:wght@400;700&display=swap">
<style>
  :root {
    --backdrop: #dde3e7;
    --card: #ffffff;
    --green: #00a650;
    --lime: #8dc63f;
    --white: #ffffff;
    --phone-red: #d71f26;
    --photo-light: #d9b98f;
    --photo-dark: #7a5a3f;
  }
  html, body {
    margin: 0;
    padding: 0;
    width: 1200px;
    height: 882px;
    overflow: hidden;
    background: var(--backdrop);
  }
  .business-card {
    position: absolute;
    left: 75px;
    top: 125px;
    width: 1050px;
    height: 631px;
    box-shadow: 0 6px 18px rgba(0, 0, 0, 0.18);
  }
  .business-card svg {
    display: block;
    width: 100%;
    height: 100%;
    font-family: "Arimo", Arial, sans-serif;
  }
  .card-bg { fill: var(--card); }
  .band-green { fill: var(--green); }
  .band-lime { fill: var(--lime); }
  .name { fill: var(--white); font-weight: 700; font-size: 18.5px; }
  .role { fill: var(--white); font-size: 14px; }
  .handle { fill: var(--green); font-size: 15px; }
  .contact-line { fill: var(--white); font-size: 15px; }
  .contact-small { fill: var(--white); font-size: 14px; }
  .icon-box-green { fill: var(--white); stroke: var(--green); stroke-width: 1.6; }
  .icon-box-white { fill: var(--green); stroke: var(--white); stroke-width: 1.6; }
  .icon-inner { fill: none; stroke: var(--white); stroke-width: 1.2; }
  .icon-inner-green { fill: none; stroke: var(--green); stroke-width: 1.2; }
  .phone-number { fill: var(--white); font-size: 15px; letter-spacing: 4px; }
  .phone-box { fill: var(--white); stroke: var(--white); }
  .phone-glyph { fill: var(--phone-red); }
</style>
</head>
<body>
<div class="business-card">
  <svg viewBox="0 0 521 313" xmlns="http://www.w3.org/2000/svg">
    <defs>
      <linearGradient id="portrait-tone" x1="0" y1="0" x2="1" y2="1">
        <stop offset="0" stop-color="var(--photo-dark)"/>
        <stop offset="0.5" stop-color="var(--photo-light)"/>
        <stop offset="1" stop-color="#3b3f8f"/>
      </linearGradient>
    </defs>

    <rect class="card-bg" x="0" y="0" width="521" height="313"/>

    <!-- portrait area -->
    <polygon role="img" aria-label="Portrait photo of Rosalind, smiling"
             fill="url(#portrait-tone)"
             points="0,78 205,78 271,313 66,313 0,80"/>

    <!-- header band -->
    <polygon class="band-lime" points="286,19 302,19 329,78 312,78"/>
    <polygon class="band-green" points="0,19 286,19 312,78 0,78"/>
    <text class="name" x="37" y="49">Your Name</text>
    <text class="role" x="37" y="69">Positions</text>

    <!-- chirpr handle -->
    <text class="handle" x="463" y="66" text-anchor="end">@ThePalermoNotes</text>
    <rect class="icon-box-green" x="470" y="48" width="25" height="25"/>
    <rect class="icon-inner-green" x="473" y="51" width="19" height="19"/>

    <!-- contact panel -->
    <polygon class="band-green" points="209,85 521,85 521,242 253,242"/>

    <g class="contact-list">
      <text class="contact-line" x="463" y="106" text-anchor="end">Rosalind_Q.K</text>
      <rect class="icon-box-white" x="470" y="89" width="25" height="25"/>
      <rect class="icon-inner" x="473" y="92" width="19" height="19"/>

      <text class="contact-line" x="463" y="137" text-anchor="end" textLength="238" lengthAdjust="spacingAndGlyphs">/channel/QRpLwVn4kZ-mTHbyqo8erxt7B</text>
      <rect class="icon-box-white" x="470" y="119" width="25" height="25"/>
      <rect class="icon-inner" x="473" y="122" width="19" height="19"/>

      <text class="contact-line" x="463" y="168" text-anchor="end">kbellin@mx.ovrk.edu</text>
      <rect class="icon-box-white" x="470" y="150" width="25" height="25"/>
      <rect class="icon-inner" x="473" y="153" width="19" height="19"/>

      <text class="contact-line" x="463" y="199" text-anchor="end">/rosalind.bellin.71924</text>
      <rect class="icon-box-white" x="470" y="181" width="25" height="25"/>
      <rect class="icon-inner" x="473" y="184" width="19" height="19"/>

      <text class="contact-small" x="463" y="221" text-anchor="end" textLength="208" lengthAdjust="spacingAndGlyphs">https://www.craftlo-example.com/shop/</text>
      <text class="contact-small" x="463" y="236" text-anchor="end">RosasTp?ref=pr_shop_more</text>
      <rect class="icon-box-white" x="470" y="211" width="25" height="25"/>
      <rect class="icon-inner" x="473" y="214" width="19" height="19"/>
    </g>

    <!-- phone band -->
    <polygon class="band-lime" points="351,249 369,249 386,302 367,302"/>
    <polygon class="band-green" points="0,249 351,249 369,302 0,302"/>
    <rect class="phone-box" x="70" y="262" width="24" height="24"/>
    <rect class="icon-inner-green" x="72" y="264" width="20" height="20"/>
    <path class="phone-glyph"
          d="M76.5 268.5 l3 -1.5 l2 3.5 l-1.6 1.2 q1 2.4 3.4 3.6 l1.3 -1.6 l3.4 2 l-1.4 3 q-5 0 -8.6 -4.2 q-2.6 -3 -1.5 -6 z"/>
    <text class="phone-number" x="109" y="279">417-552-8904</text>
  </svg>
</div>
</body>
</html>
```